Financial Advisor Website Design

We are working with KLV•ARO. They are a financial advising company that needs a new website design.

Some sites to use for inspiration:

https://investor.quillmarsh.com
https://www.hollisbrant.com/us-en
https://www.corvantel.com
https://www.aboutpellgrew.com

Thank you for taking the time to consider designing a website for us. We are web developers based in Stockton and Los Angeles, CA, USA. Most of our projects go through the same process. Understanding this process may help you win a project with us. We custom-code all of our websites in-house. We don’t have any requirements as to what tools you use for your design, but we prefer Figma files. For any design that we label as four-stars, we send it to the client for review. The client picks the final design they want us to use. Once we complete this process, we will continue to show additional clients all the four-star sites and purchase them later. Your designs will have multiple chances to sell. For better chances of success, we ask that you follow these guidelines.

IMAGES:
If you use any images or icons in the design, we ask that you have a link to the asset so we can purchase the image/icon. Most of the designs we submit do not have the customer’s images on them unless they have some great images. Be creative; show us the feeling you are trying to portray with your image choices. Use any royalty-free site you choose. We subscribe to Parvel and mainly use their images, but we can purchase images outside of Parvel.

PLEASE NOTE: we will not submit designs to clients with watermarks on the images.

FONTS:
We ask that you identify the fonts used in the design. This can be done in a message if you want. We typically use Tessly Fonts and Parvel Fonts.

CONTENT:
We're always open to different content and ideas. We often submit designs with stock images so the client can see our vision. We typically take pictures after the website launch to use their images with our vision. Lorem Ipsum is fine for paragraphs, but we ask that you write the headers in correct English. We want to be able to show the vision and identify the sections of the website.

INSPIRATION:
We typically add a couple of links in the brief of websites we like to help you get started in your design.

REVISIONS:
We do not often ask for revisions of the designs unless we see something in the design that may not appeal to the client. If there are slight changes that we want to make, we do that in the development process.

FEEDBACK:
We rarely give feedback on designs during the design process. We are working on many website projects and do not have the time to provide feedback. We usually respond if your request is well thought out and asks specific questions, but a note asking “feedback, please” usually goes unanswered.

```html
<!DOCTYPE html>
<html lang="en">
<head>
<meta charset="utf-8">
<title>KLV•ARO — Your goals, our guidance</title>
<link href="https://fonts.googleapis.com/css2?family=Newsreader:opsz,wght@6..72,400;6..72,500&family=Inter:wght@400;500&display=swap" rel="stylesheet">
<style>
:root{
  --navy:#163f74;
  --navy-deep:#0f2c52;
  --blue:#2f5e92;
  --gold:#e6c22f;
  --ink:#14213a;
  --text:#26324a;
  --muted:#5f6b7d;
  --card:#e9eef3;
  --panel:#e5ebf1;
  --footer:#dfe6ee;
  --line:#d8c88a;
  --white:#ffffff;
}
*{box-sizing:border-box;margin:0;padding:0}
html,body{width:1200px;height:4878px;overflow:hidden}
body{background:var(--white);font-family:"Inter",Helvetica,Arial,sans-serif;color:var(--text);position:relative}
.serif{font-family:"Newsreader",Georgia,serif;font-weight:400;color:var(--ink)}
a{color:inherit;text-decoration:none}
.abs{position:absolute}

/* header */
.site-header{position:absolute;top:0;left:0;width:1200px;height:70px;z-index:3}
.brand{position:absolute;left:53px;top:24px;font-family:"Newsreader",Georgia,serif;font-size:22px;font-weight:500;letter-spacing:4px;color:var(--navy)}
.main-nav{position:absolute;top:27px;left:686px;display:flex;gap:0;font-size:13px;color:var(--ink)}
.main-nav a{margin-right:34px;display:flex;align-items:center;gap:6px}
.main-nav svg{width:9px;height:9px}

/* hero */
.hero{position:absolute;top:70px;left:0;width:1200px;height:650px;
  background:linear-gradient(180deg,#dde4ec 0%,#eef2f6 55%,#ffffff 100%)}
.hero-visual{position:absolute;right:0;top:0;width:720px;height:650px;
  background:radial-gradient(ellipse at 70% 30%,#9aa6b6 0%,#c7d0db 35%,#e6ebf1 70%,rgba(255,255,255,0) 100%)}
.hero h1{position:absolute;left:53px;top:180px;font-size:62px;line-height:72px}
.hero p{position:absolute;left:53px;top:343px;width:360px;font-size:16px;line-height:25px;color:var(--text)}
.btn{display:inline-flex;align-items:center;justify-content:center;border-radius:30px;font-size:12px}
.btn-navy{background:var(--navy);color:#fff}
.btn-gold{background:var(--gold);color:var(--ink)}
.hero .btn{position:absolute;left:53px;top:450px;width:126px;height:43px}

/* products */
.section-title{font-size:36px;line-height:44px}
.products-title{position:absolute;left:53px;top:866px}
.product-cards{position:absolute;left:53px;top:997px;display:flex;gap:20px}
.product-card{width:258px;height:323px;background:var(--card);border-radius:4px;padding:28px 20px}
.product-card svg.icon{width:72px;height:72px;margin-left:0}
.product-card h3{font-size:21px;margin:26px 0 12px}
.product-card p{font-size:12px;line-height:19px;color:var(--text);height:100px}
.learn{display:flex;align-items:center;gap:10px;font-size:12px;color:var(--ink)}
.learn svg{width:18px;height:10px}

/* advisors band */
.advisors{position:absolute;left:53px;top:1446px;width:1093px;height:540px;display:flex}
.advisors-copy{width:469px;background:var(--navy);padding:100px 40px 0}
.advisors-copy h2{color:#fff;font-size:50px;line-height:58px}
.advisors-copy p{color:#dbe4ef;font-size:13px;line-height:21px;margin:22px 0 28px;width:330px}
.advisors-copy .btn{width:126px;height:42px}
.advisors-photo{flex:1;background:linear-gradient(135deg,#e7ebee 0%,#cfd6dc 45%,#9fb3c4 70%,#e2e6ea 100%)}

/* stats */
.stats{position:absolute;left:0;top:2050px;width:1200px;height:520px;
  background:linear-gradient(180deg,#fff 0%,#fff 50%,#e9edf2 85%,#fff 100%)}
.stats-title{position:absolute;left:61px;top:66px}
.stat{position:absolute;top:200px;width:325px}
.stat .num{font-size:92px;line-height:100px;letter-spacing:-2px}
.stat .label{font-size:12px;margin-top:16px;padding-bottom:8px;border-bottom:1px solid var(--line)}
.stat .desc{font-size:13px;line-height:21px;margin-top:15px;width:320px}

/* testimonial */
.testimonial{position:absolute;left:53px;top:2726px;width:1093px;height:534px;display:flex}
.testimonial-photo{width:547px;background:linear-gradient(160deg,#efeee9 0%,#d9d3c8 45%,#b9a594 75%,#e6e2dc 100%)}
.testimonial-copy{flex:1;background:var(--panel);padding:48px 40px}
.testimonial-copy h2{font-size:50px;line-height:58px}
.quote-mark{font-family:"Newsreader",Georgia,serif;font-size:64px;color:#c9a63a;line-height:1;margin-top:34px;height:44px}
.testimonial-copy p{font-size:13px;line-height:22px;width:450px;margin-top:6px}
.author{font-size:13px;margin-top:14px}
.arrows{display:flex;gap:12px;margin-top:22px}
.arrows svg{width:34px;height:34px}

/* cta */
.cta{position:absolute;left:53px;top:3362px;width:1093px;height:373px;
  background:linear-gradient(180deg,#2f5e92 0%,#2f5e92 55%,#3a6a9d 80%,#2b5686 100%);padding:60px 41px}
.cta h2{color:#fff;font-size:50px;line-height:58px}
.cta .btn{margin-top:18px;width:160px;height:42px}

/* news */
.news-title{position:absolute;left:53px;top:3860px}
.view-all{position:absolute;left:1010px;top:3860px;width:136px;height:43px;border:1px solid var(--navy);border-radius:30px;font-size:12px;display:flex;align-items:center;justify-content:center;color:var(--ink)}
.news-cards{position:absolute;left:53px;top:3955px;display:flex;gap:24px}
.news-card{width:255px;height:375px;background:#f1f4f7;border-radius:4px;overflow:hidden}
.news-card .thumb{height:213px}
.news-card h3{font-size:17px;line-height:20px;padding:26px 26px 0;height:86px}
.news-card .learn{padding:14px 26px 0}

/* footer */
.site-footer{position:absolute;left:0;top:4415px;width:1200px;height:463px;background:var(--footer)}
.footer-col{position:absolute;top:63px;font-size:12px;color:var(--ink)}
.footer-col h4{font-weight:400;color:var(--muted);font-size:12px;margin-bottom:32px}
.footer-col li{list-style:none;margin-bottom:15px}
.footer-brand{position:absolute;left:53px;top:300px;font-family:"Newsreader",Georgia,serif;font-size:20px;font-weight:500;letter-spacing:4px;color:var(--navy)}
.socials{position:absolute;left:200px;top:303px;display:flex;gap:12px}
.socials span{width:15px;height:15px;border-radius:50%;background:#6b7a8d;display:block}
.disclaimer{position:absolute;left:53px;top:360px;width:1093px;font-size:10px;line-height:16px;color:var(--muted)}
.legal{position:absolute;left:53px;top:430px;font-size:10px;color:var(--muted);display:flex;gap:14px}
</style>
</head>
<body>

<header class="site-header">
  <a class="brand" href="#">KLV•ARO</a>
  <nav class="main-nav">
    <a href="#">Home</a>
    <a href="#">Solutions</a>
    <a href="#">Planning <svg viewBox="0 0 10 10"><path d="M1 3l4 4 4-4" fill="none" stroke="#14213a" stroke-width="1.2"/></svg></a>
    <a href="#">Insights <svg viewBox="0 0 10 10"><path d="M1 3l4 4 4-4" fill="none" stroke="#14213a" stroke-width="1.2"/></svg></a>
    <a href="#">News</a>
    <a href="#">Contact us</a>
  </nav>
</header>

<section class="hero">
  <div class="hero-visual" role="img" aria-label="Snow-covered mountain peak under a pale sky"></div>
  <h1 class="serif">Your goals,<br>our guidance</h1>
  <p>Practical, advisor-led planning for life’s priorities, emergency funds, big purchases, college, retirement, and everything in between.</p>
  <a class="btn btn-navy" href="#">Get Started</a>
</section>

<h2 class="section-title serif products-title">Products and accounts<br>that fit your goals</h2>
<div class="product-cards">
  <article class="product-card">
    <svg class="icon" viewBox="0 0 72 72" fill="none" stroke="#3a4658" stroke-width="1.4"><circle cx="32" cy="40" r="22"/><text x="32" y="47" font-size="20" text-anchor="middle" fill="#3a4658" stroke="none" font-family="Inter,sans-serif">$</text><path d="M44 8a20 20 0 0 1 20 20H44z" fill="#e6c22f"/></svg>
    <h3 class="serif">Brokerage &amp; Cash</h3>
    <p>Open a flexible brokerage account with transparent pricing, intuitive research, and built-in cash management to keep your money working between trades.</p>
    <a class="learn" href="#">Learn more <svg viewBox="0 0 18 10"><path d="M0 5h16M12 1l4 4-4 4" fill="none" stroke="#14213a" stroke-width="1.2"/></svg></a>
  </article>
  <article class="product-card">
    <svg class="icon" viewBox="0 0 72 72" fill="none" stroke="#3a4658" stroke-width="1.4"><circle cx="36" cy="36" r="30"/><rect x="16" y="26" width="40" height="20" rx="2" fill="#e6c22f"/><circle cx="36" cy="36" r="6"/></svg>
    <h3 class="serif">IRAs &amp; Rollovers</h3>
    <p>Choose Traditional or Roth IRAs and streamline rollovers with clear contribution rules, distribution guidance, and tax-aware support at every step.</p>
    <a class="learn" href="#">Learn more <svg viewBox="0 0 18 10"><path d="M0 5h16M12 1l4 4-4 4" fill="none" stroke="#14213a" stroke-width="1.2"/></svg></a>
  </article>
  <article class="product-card">
    <svg class="icon" viewBox="0 0 72 72" fill="none" stroke="#3a4658" stroke-width="1.4"><circle cx="36" cy="36" r="11"/><text x="36" y="41" font-size="14" text-anchor="middle" fill="#3a4658" stroke="none" font-family="Inter,sans-serif">$</text><path d="M36 25V8M36 47v17M25 36H8M47 36h17M28 28L16 16M44 44l12 12M44 28l12-12M28 44L16 56"/><circle cx="36" cy="8" r="3" fill="#e6c22f"/><circle cx="64" cy="36" r="3" fill="#e6c22f"/><circle cx="8" cy="36" r="3"/><circle cx="36" cy="64" r="3"/></svg>
    <h3 class="serif">Managed Portfolios</h3>
    <p>Get a diversified, professionally managed mix tailored to your risk level and timeline, with ongoing monitoring and periodic rebalancing.</p>
    <a class="learn" href="#">Learn more <svg viewBox="0 0 18 10"><path d="M0 5h16M12 1l4 4-4 4" fill="none" stroke="#14213a" stroke-width="1.2"/></svg></a>
  </article>
  <article class="product-card">
    <svg class="icon" viewBox="0 0 72 72" fill="none" stroke="#3a4658" stroke-width="1.4"><rect x="10" y="12" width="40" height="52" rx="2"/><path d="M18 26h4M26 26h16M18 36h4M26 36h16M18 46h4M26 46h16M18 56h4M26 56h10"/><path d="M40 14l14-6 14 6-14 6z" fill="#e6c22f"/></svg>
    <h3 class="serif">529 &amp; HSA</h3>
    <p>Use tax-smart accounts to fund education and healthcare, with straightforward setup, flexible contributions, and options to invest for long-term needs.</p>
    <a class="learn" href="#">Learn more <svg viewBox="0 0 18 10"><path d="M0 5h16M12 1l4 4-4 4" fill="none" stroke="#14213a" stroke-width="1.2"/></svg></a>
  </article>
</div>

<section class="advisors">
  <div class="advisors-copy">
    <h2 class="serif">Advisors who<br>meet you where<br>you are</h2>
    <p>From first plan to retirement income, get actionable steps and support tailored to your timeline and risk comfort.</p>
    <a class="btn btn-gold" href="#">Get Started</a>
  </div>
  <div class="advisors-photo" role="img" aria-label="An advisor meeting with a couple around a table with a laptop"></div>
</section>

<section class="stats">
  <h2 class="section-title serif stats-title">Measurable progress,<br>real impact</h2>
  <div class="stat" style="left:61px">
    <div class="num serif">92%</div>
    <div class="label">Plan adherence at 12 months</div>
    <div class="desc">Clients who followed recommended savings rates and portfolio ranges for at least four quarterly check-ins.</div>
  </div>
  <div class="stat" style="left:432px">
    <div class="num serif">87%</div>
    <div class="label">Stayed invested during volatility</div>
    <div class="desc">Clients maintained target allocations within defined bands during a major market pullback.</div>
  </div>
  <div class="stat" style="left:802px">
    <div class="num serif">3.1%</div>
    <div class="label">Average fee savings identified</div>
    <div class="desc">Household audits found opportunities by consolidating accounts and selecting lower-cost vehicles where appropriate.</div>
  </div>
</section>

<section class="testimonial">
  <div class="testimonial-photo" role="img" aria-label="Portrait of a client standing by a bright window"></div>
  <div class="testimonial-copy">
    <h2 class="serif">Why partner with<br>KLV Aro</h2>
    <div class="quote-mark">“</div>
    <p>What stood out was how our advisor connected the dots across budgeting, debt, insurance, college, and retirement—not just investments. We now have a single plan with automatic savings, guardrails for big decisions, and a cadence that keeps us accountable. When markets were noisy, the plan didn’t change—our confidence did.</p>
    <div class="author">Dana Whitcombe</div>
    <div class="arrows">
      <svg viewBox="0 0 34 34" fill="none" stroke="#14213a" stroke-width="1.2"><circle cx="17" cy="17" r="16"/><path d="M24 17H10M14 13l-4 4 4 4"/></svg>
      <svg viewBox="0 0 34 34" fill="none" stroke="#14213a" stroke-width="1.2"><circle cx="17" cy="17" r="16"/><path d="M10 17h14M20 13l4 4-4 4"/></svg>
    </div>
  </div>
</section>

<section class="cta" role="region" aria-label="Talk to an advisor">
  <h2 class="serif">Let’s turn your financial goals into<br>a clear plan today</h2>
  <a class="btn btn-gold" href="#">Talk to an Advisor</a>
</section>

<h2 class="section-title serif news-title">News and insights</h2>
<a class="view-all" href="#">View all news</a>
<div class="news-cards">
  <article class="news-card">
    <div class="thumb" role="img" aria-label="Hands working with a calculator and notebook" style="background:linear-gradient(135deg,#f1ece4,#cdbfae 60%,#8d98a6)"></div>
    <h3 class="serif">Navigating year-end planning: taxes, timing, and transfers</h3>
    <a class="learn" href="#">Learn more <svg viewBox="0 0 18 10"><path d="M0 5h16M12 1l4 4-4 4" fill="none" stroke="#14213a" stroke-width="1.2"/></svg></a>
  </article>
  <article class="news-card">
    <div class="thumb" role="img" aria-label="Bronze bull statue on a city street" style="background:linear-gradient(160deg,#9aa1a8,#4d4a45 55%,#2d2a27)"></div>
    <h3 class="serif">Market pulse: what this week’s moves could mean for long-term plans</h3>
    <a class="learn" href="#">Learn more <svg viewBox="0 0 18 10"><path d="M0 5h16M12 1l4 4-4 4" fill="none" stroke="#14213a" stroke-width="1.2"/></svg></a>
  </article>
  <article class="news-card">
    <div class="thumb" role="img" aria-label="Hand stacking coins on a blue background" style="background:linear-gradient(160deg,#7fa3cf,#4f79ae 60%,#b8975a)"></div>
    <h3 class="serif">Starting strong: a practical path from first deposit to diversified core</h3>
    <a class="learn" href="#">Learn more <svg viewBox="0 0 18 10"><path d="M0 5h16M12 1l4 4-4 4" fill="none" stroke="#14213a" stroke-width="1.2"/></svg></a>
  </article>
  <article class="news-card">
    <div class="thumb" role="img" aria-label="Tablet showing charts beside a coffee cup" style="background:linear-gradient(160deg,#c9ccd0,#7b8794 55%,#3f4a58)"></div>
    <h3 class="serif">Smart moves before year-end: contributions, and conversions</h3>
    <a class="learn" href="#">Learn more <svg viewBox="0 0 18 10"><path d="M0 5h16M12 1l4 4-4 4" fill="none" stroke="#14213a" stroke-width="1.2"/></svg></a>
  </article>
</div>

<footer class="site-footer">
  <div class="footer-col" style="left:53px"><h4>Solutions</h4><ul><li>Brokerage &amp; Cash</li><li>IRAs &amp; Rollovers</li><li>Managed Portfolios</li><li>529</li><li>HSA</li></ul></div>
  <div class="footer-col" style="left:338px"><h4>Planning</h4><ul><li>Goal Planning</li><li>Retirement Income</li><li>Tax-aware Strategies</li><li>Rollovers</li></ul></div>
  <div class="footer-col" style="left:623px"><h4>Insights</h4><ul><li>Guides</li><li>Webinars</li><li>Market Sense Weekly</li></ul></div>
  <div class="footer-col" style="left:908px"><h4>Company &amp; News</h4><ul><li>About</li><li>Careers</li><li>News</li><li>Contact</li></ul></div>
  <div class="footer-brand">KLV•ARO</div>
  <div class="socials" aria-label="Social links"><span></span><span></span><span></span></div>
  <p class="disclaimer">Investing involves risk, including loss of principal. Diversification does not ensure a profit or protect against loss. Past performance is not a guarantee of future results. Advisory services and brokerage services are distinct and may have different fees and obligations; see Form CRS and disclosures.</p>
  <div class="legal"><span>© 2025 KLV Aro. All rights reserved.</span><span>Terms</span><span>Privacy</span></div>
</footer>

</body>
</html>
```